Ad for regional magazine for startup "Varumo"

We need a small ad for a small German regional magazine for our startup company Varumo which provides on-premise service for all kind of electronic problems.

We also need the Indesign files to be able to make minor changes (e.g. the phone number) in the future.

An example ad that we used before (for another region with another phone number) is attached.

Industry/Entity Type

Technical Service

Requirements
Must have
• Needed contents:
• "Elektronik-Problem?" (Electronic problem?)
• "Ihr Media-Pannenhelfer kommt" (Your media helper comes)
• "TV, Video, Telefon, Smartphone, Internet, Computer"
• "Terminbuchung: 07041-3926518" (booking)
• "Soforthilfe - auch abends und am Wochenende" (immediate help - also in the evenings and at the weekend)
• "www.varumo.de"
• logo
• picture
• Size: 90mm (width) x 50-70mm (height)
• Font & colors: see attachment

```html
<!DOCTYPE html>
<html lang="de">
<head>
<meta charset="utf-8">
<title>Varumo – Anzeige</title>
<link rel="stylesheet" href="https://fonts.googleapis.com/css2?family=Oswald:wght@400;700&family=Questrial&display=swap">
<style>
  :root {
    --green: #52a844;
    --charcoal: #3e4444;
    --text-dark: #2f3333;
    --white: #ffffff;
    --stage: #1e1e1e;
    --photo-light: #e9e6e1;
    --photo-mid: #c9c2b6;
  }
  * { margin: 0; padding: 0; box-sizing: border-box; }
  html, body {
    width: 1200px; height: 900px; overflow: hidden;
    background: var(--stage);
  }
  .ad {
    position: absolute; left: 100px; top: 62px;
    width: 1002px; height: 776px;
    background: var(--white);
    overflow: hidden;
    font-family: "Questrial", sans-serif;
  }
  .headline {
    position: absolute; left: 0; right: 0; top: 14px;
    text-align: center;
    font-family: "Oswald", sans-serif; font-weight: 700;
    font-size: 98px; line-height: 1;
    color: var(--green);
    letter-spacing: 1px;
    transform: scaleX(0.96);
  }
  .tagline-bar {
    position: absolute; left: 85px; top: 116px;
    width: 832px; height: 44px;
    background: var(--charcoal);
    display: flex; align-items: center; justify-content: center; gap: 14px;
  }
  .tagline-bar .rule {
    width: 70px; height: 2px;
    background: linear-gradient(90deg, rgba(255,255,255,0), var(--white));
  }
  .tagline-bar .rule.right {
    background: linear-gradient(90deg, var(--white), rgba(255,255,255,0));
  }
  .tagline {
    font-family: "Questrial", sans-serif;
    font-size: 33px; color: var(--white);
    letter-spacing: 0.5px;
  }
  .services {
    position: absolute; left: 0; right: 0; top: 170px;
    text-align: center;
    font-size: 35px; color: var(--text-dark);
    letter-spacing: 0.3px;
  }
  .divider-shapes {
    position: absolute; left: 0; top: 228px;
    width: 1002px; height: 48px;
  }
  .photo {
    position: absolute; left: 0; top: 278px;
    width: 1002px; height: 328px;
    background: linear-gradient(90deg, var(--photo-mid) 0%, var(--photo-light) 45%, #dcd6cc 75%, #c8b89e 100%);
  }
  .footer-shapes {
    position: absolute; left: 0; top: 606px;
    width: 1002px; height: 170px;
  }
  .logo {
    position: absolute; left: 42px; top: 664px;
    display: flex; align-items: center; gap: 14px;
    font-family: "Questrial", sans-serif;
    font-size: 76px; line-height: 1;
    color: var(--charcoal);
    letter-spacing: 2px;
  }
  .logo .dot {
    width: 18px; height: 18px; border-radius: 50%;
    background: var(--green);
  }
  .contact {
    position: absolute; left: 426px; top: 636px; width: 542px;
    color: var(--white);
  }
  .booking {
    font-family: "Oswald", sans-serif; font-weight: 700;
    font-size: 37px; line-height: 1; letter-spacing: 0.5px;
    white-space: nowrap;
  }
  .hours {
    margin-top: 12px;
    font-size: 23px; letter-spacing: 0.2px;
    white-space: nowrap;
  }
  .web {
    margin-top: 12px;
    border-top: 2px solid var(--white);
    border-bottom: 2px solid var(--white);
    padding: 6px 0 7px;
    font-size: 15.5px; letter-spacing: 4.1px;
    white-space: nowrap;
  }
</style>
</head>
<body>
  <div class="ad">
    <h1 class="headline">ELEKTRONIK-PROBLEM?</h1>

    <div class="tagline-bar">
      <span class="rule"></span>
      <span class="tagline">IHR MEDIA-PANNENHELFER KOMMT</span>
      <span class="rule right"></span>
    </div>

    <p class="services">TV, Video, Telefon, Smartphone, Internet, Computer</p>

    <svg class="divider-shapes" viewBox="0 0 1002 48" aria-hidden="true">
      <polygon points="0,2 380,35 0,35" fill="var(--green)"/>
      <polygon points="1002,2 622,35 1002,35" fill="var(--green)"/>
      <rect x="0" y="35" width="1002" height="11" fill="var(--charcoal)"/>
    </svg>

    <div class="photo" role="img" aria-label="Foto: Ein Servicetechniker im grauen Poloshirt erklärt einem älteren Herrn am Esstisch ein Tablet, im Hintergrund helles Fenster und eine Obstschale"></div>

    <svg class="footer-shapes" viewBox="0 0 1002 170" aria-hidden="true">
      <rect x="0" y="4" width="1002" height="10" fill="var(--charcoal)"/>
      <path d="M368,14 L1002,14 L1002,170 L392,170 Q370,95 368,14 Z" fill="var(--charcoal)"/>
      <path d="M384,14 L1002,14 L1002,170 L408,170 Q386,95 384,14 Z" fill="var(--green)"/>
    </svg>

    <div class="logo">
      <span class="logo-name">Varumo</span>
      <span class="dot"></span>
    </div>

    <div class="contact">
      <p class="booking">TERMINBUCHUNG: 07041-3926518</p>
      <p class="hours">Soforthilfe - auch abends und am Wochenende</p>
      <p class="web">For more information vist www.varumo.de</p>
    </div>
  </div>
</body>
</html>
```